social interest sharing site needs a web site design

we need a web site design for a social web platform.
the site is one page(main page), that is split into 3 sections
each section is a different color(red,green and blue)
and a user can choose to share each of the sections.
any section/color will contain boxes , each box can contain different media types.

the media types:
* list of URLS
* list of articles including title + image + description
* list of videos
* thumbnails of images
* calender
* list of emails

the main content will look like corkboardly layout
multiple boxes each box can contain different type of content as described above

each color is a different tab
each tab will have layout like corkboardly
Updates

please read the last description update.
and i uploaded an image that can explain the requirements better

thanks
Oren
 

Industry/Entity Type

Media

```html
<!DOCTYPE html>
<html lang="en">
<head>
<meta charset="utf-8">
<title>tessaly.me</title>
<link href="https://fonts.googleapis.com/css2?family=Open+Sans:wght@400;600;700&display=swap" rel="stylesheet">
<style>
:root{
  --ink-dark:#2f2f2f;
  --bar:#3a3a3a;
  --teal:#45c8a8;
  --blue:#5ba0e0;
  --coral:#fb7373;
  --red:#cc1f1f;
  --red-btn:#f26a6a;
  --green:#2ecc71;
  --green-dark:#1fa85a;
  --sky:#2fa8e0;
  --sky-dark:#1f86bf;
  --circle:#3f444c;
  --white:#ffffff;
  --text-grey:#666666;
}
*{box-sizing:border-box;margin:0;padding:0}
html,body{width:702px;height:1200px;overflow:hidden}
body{position:relative;font-family:"Open Sans",Arial,sans-serif;color:var(--white);background:var(--coral)}
.abs{position:absolute}

.topbar{left:0;top:0;width:702px;height:48px;background:var(--ink-dark)}
.brand{left:64px;top:13px;font-weight:600;font-size:16px;color:var(--white)}
.social{left:420px;top:16px;display:flex;gap:5px}
.social span{width:18px;height:18px;border-radius:2px}
.btn-top{top:16px;height:18px;font-size:10px;line-height:18px;text-align:center;border-radius:2px}
.signup{left:518px;width:56px;background:#14b14a}
.login{left:581px;width:57px;background:#e6e6e6;color:#444}

.subbar{left:0;top:48px;width:702px;height:42px;background:var(--bar)}
.gear{left:6px;top:58px}
.tab{top:58px;height:21px;font-size:10px;font-weight:600;line-height:21px;text-align:center;border-radius:2px}
.tab-videos{left:366px;width:76px;background:var(--red-btn)}
.tab-pics{left:451px;width:77px;background:#5b9ee0}
.tab-calendar{left:536px;width:102px;background:#3cc9a4}

.hero{left:0;top:90px;width:702px;height:268px;background:linear-gradient(120deg,#5fd3b6,var(--teal) 45%,#3cbf9e)}
.hero-title{left:65px;top:200px;font-size:21px;font-weight:700}
.hero-text{left:65px;top:238px;width:190px;font-size:9.4px;line-height:12.5px}
.join{left:65px;top:298px;width:99px;height:28px;background:#e54848;border-radius:3px;font-size:12px;font-weight:600;display:flex;align-items:center;justify-content:center;gap:6px;box-shadow:0 2px 0 #b83232}
.device{left:280px;top:118px;width:358px;height:240px;border-radius:10px 10px 0 0;background:#1c1c1c;padding:16px 16px 0}
.device-screen{width:100%;height:100%;background:linear-gradient(180deg,#a52a2a,#8e2323)}

.media{left:0;top:358px;width:702px;height:286px;background:var(--blue)}
.section-title{width:702px;left:0;text-align:center;font-size:22px;font-weight:700}
.section-text{left:46px;width:610px;text-align:center;font-size:10.2px;line-height:14px}
.type{top:488px;width:100px;text-align:center}
.type-circle{width:99px;height:99px;border-radius:50%;background:var(--circle);display:flex;align-items:center;justify-content:center;margin:0 auto}
.type-photo{background:radial-gradient(circle,#7a6a62,#3a3434)}
.type-label{margin-top:19px;font-size:11.5px;font-weight:600}

.card{background:var(--white);width:138px}
.card-img{width:138px;height:102px}
.card-title{color:var(--red);font-size:9.5px;padding:7px 5px 0}
.card-text{color:var(--text-grey);font-size:7px;line-height:9px;padding:5px 5px 0}
.go{position:absolute;right:0;bottom:0;width:19px;height:17px;background:var(--red);display:flex;align-items:center;justify-content:center}
.note{width:139px;padding:8px 5px 0;color:var(--white)}
.note-green{background:var(--green)}
.note-green .go{background:var(--green-dark)}
.note-blue{background:var(--sky)}
.note-blue .go{background:var(--sky-dark)}
.note .t{font-size:9.5px;font-weight:600}
.note .d{font-size:7px;line-height:9px;margin-top:3px;padding-right:20px}

.footer{left:0;top:1176px;width:702px;height:24px;background:var(--ink-dark);font-size:7.5px;text-align:center;line-height:24px}
</style>
</head>
<body>

<header class="abs topbar"></header>
<div class="abs brand">tessaly.me</div>
<div class="abs social">
  <span style="background:#3b5998"></span>
  <span style="background:#4cc2e8"></span>
  <span style="background:#f08a24"></span>
  <span style="background:#f2f2f2"></span>
</div>
<div class="abs btn-top signup">Sign Up</div>
<div class="abs btn-top login">Login</div>

<nav class="abs subbar"></nav>
<svg class="abs gear" width="22" height="22" viewBox="0 0 22 22"><circle cx="11" cy="11" r="6" fill="none" stroke="#fff" stroke-width="4" stroke-dasharray="3 2"/><circle cx="11" cy="11" r="4" fill="#fff"/><circle cx="11" cy="11" r="2" fill="#3a3a3a"/></svg>
<div class="abs tab tab-videos">Add Videos</div>
<div class="abs tab tab-pics">Dana's Pics +</div>
<div class="abs tab tab-calendar">Calender &amp; Notes</div>

<section class="abs hero" role="img" aria-label="Teal-tinted photo of a person holding a phone"></section>
<h1 class="abs hero-title">tessaly.me</h1>
<p class="abs hero-text">Lorem ipsum dolor sit amet, consectetur adipisicing elit, sed do eiusmod tempor incididunt ut labore et dolore magna aliqua...</p>
<div class="abs join">Join Now <svg width="13" height="13" viewBox="0 0 13 13"><circle cx="6.5" cy="6.5" r="6.5" fill="#fff"/><path d="M3.5 6.5h5M6.5 4l2.5 2.5L6.5 9" stroke="#e54848" stroke-width="1.6" fill="none"/></svg></div>
<div class="abs device"><div class="device-screen" role="img" aria-label="Screen preview of the articles board"></div></div>

<section class="abs media"></section>
<h2 class="abs section-title" style="top:384px">The Media Types</h2>
<p class="abs section-text" style="top:418px">Lorem ipsum dolor sit amet, consectetur adipisicing elit, sed do eiusmod tempor incididunt utlabore et dolore magna aliqua.<br>Ut enim ad minim veniam,quis nostrud exercitation ullamco laboris nisi ut aliquip ex ea commodo consequat duis aute<br>irure dolor in reprehenderit <u>tessaly.me</u></p>

<div class="abs type" style="left:64px">
  <div class="type-circle"><svg width="50" height="58" viewBox="0 0 50 58"><path d="M8 2h24l12 12v40H8z" fill="none" stroke="#fff" stroke-width="3"/><path d="M32 2v12h12" fill="none" stroke="#fff" stroke-width="3"/><rect x="2" y="24" width="40" height="18" rx="3" fill="#fff"/><text x="22" y="38" text-anchor="middle" font-family="Open Sans,Arial,sans-serif" font-weight="700" font-size="13" fill="#3f444c">URL</text></svg></div>
  <div class="type-label">List of URLS</div>
</div>
<div class="abs type" style="left:183px">
  <div class="type-circle"><svg width="62" height="50" viewBox="0 0 62 50"><rect x="2" y="2" width="50" height="38" fill="none" stroke="#fff" stroke-width="3"/><rect x="9" y="9" width="51" height="39" fill="#3f444c" stroke="#fff" stroke-width="3"/><path d="M14 44l13-14 8 8 6-5 14 11z" fill="#fff"/><circle cx="24" cy="20" r="4" fill="#fff"/></svg></div>
  <div class="type-label">List of Images</div>
</div>
<div class="abs type" style="left:301px">
  <div class="type-circle type-photo" role="img" aria-label="Photo of friends watching a video on a phone"><svg width="18" height="20" viewBox="0 0 18 20"><path d="M3 2l13 8-13 8z" fill="#fff"/></svg></div>
  <div class="type-label">List of Videos</div>
</div>
<div class="abs type" style="left:420px">
  <div class="type-circle"><svg width="54" height="54" viewBox="0 0 54 54"><rect x="12" y="2" width="30" height="30" fill="#fff"/><path d="M17 10h20M17 16h20M17 22h14" stroke="#3f444c" stroke-width="2"/><path d="M2 24l25 18 25-18v28H2z" fill="#fff"/></svg></div>
  <div class="type-label">List of Mails</div>
</div>
<div class="abs type" style="left:538px">
  <div class="type-circle"><svg width="48" height="52" viewBox="0 0 48 52"><rect x="2" y="6" width="44" height="44" fill="none" stroke="#fff" stroke-width="3"/><rect x="2" y="6" width="44" height="9" fill="#fff"/><path d="M10 2v8M19 2v8M29 2v8M38 2v8" stroke="#fff" stroke-width="3"/><path d="M2 24h44M2 33h44M2 42h44M13 15v35M24 15v35M35 15v35" stroke="#fff" stroke-width="2"/><rect x="25" y="25" width="9" height="7" fill="#fff"/></svg></div>
  <div class="type-label">Calender</div>
</div>

<h2 class="abs section-title" style="top:668px">Lists Of Articles</h2>
<p class="abs section-text" style="top:702px">Lorem ipsum dolor sit amet, consectetur adipisicing elit, sed do eiusmod tempor incididunt utlabore et dolore magna aliqua.<br>Ut enim ad minim veniam,quis nostrud exercitation ullamco laboris nisi ut aliquip ex ea commodo consequat duis aute<br>irure dolor in reprehenderit <u>tessaly.me</u></p>

<article class="abs card" style="left:64px;top:775px;height:191px">
  <div class="card-img" role="img" aria-label="Night photo of a performer on a street crowd" style="background:linear-gradient(160deg,#3a3a44,#14141a)"></div>
  <div class="card-title">Lorem ipsum dolor</div>
  <p class="card-text">Lorem ipsum dolor sit amet consectetur adipscing elt, Sed do euismod tempor incidunt magna aliqua...</p>
  <span class="go"><svg width="7" height="9" viewBox="0 0 7 9"><path d="M1 1l4 3.5L1 8" stroke="#fff" stroke-width="2" fill="none"/></svg></span>
</article>
<article class="abs card" style="left:64px;top:971px;height:179px">
  <div class="card-img" role="img" aria-label="Photo of a singer on a stage with audience" style="background:linear-gradient(160deg,#c94a3a,#3b3f6a)"></div>
  <div class="card-title">Lorem ipsum dolor</div>
  <p class="card-text">Lorem ipsum dolor sit amet consectetur adipscing elt, Sed do incidunt magna aliqua...</p>
  <span class="go"><svg width="7" height="9" viewBox="0 0 7 9"><path d="M1 1l4 3.5L1 8" stroke="#fff" stroke-width="2" fill="none"/></svg></span>
</article>

<article class="abs card" style="left:210px;top:775px;height:179px">
  <div class="card-img" role="img" aria-label="Photo of a woman thinking beside network icons" style="background:linear-gradient(160deg,#9a9a9a,#3a3a3a)"></div>
  <div class="card-title">Lorem ipsum dolor</div>
  <p class="card-text">Lorem ipsum dolor sit amet consectetur adipscing elt, Sed do incidunt magna aliqua...</p>
  <span class="go"><svg width="7" height="9" viewBox="0 0 7 9"><path d="M1 1l4 3.5L1 8" stroke="#fff" stroke-width="2" fill="none"/></svg></span>
</article>
<article class="abs card" style="left:210px;top:960px;height:190px">
  <div class="card-img" role="img" aria-label="Cartoon illustration of a family on a sofa" style="background:linear-gradient(160deg,#6fb6d9,#e5c9a0)"></div>
  <div class="card-title">Lorem ipsum dolor</div>
  <p class="card-text">Lorem ipsum dolor sit amet consectetur adipscing elt, Sed do euismod tempor incidunt magna aliqua...</p>
  <span class="go"><svg width="7" height="9" viewBox="0 0 7 9"><path d="M1 1l4 3.5L1 8" stroke="#fff" stroke-width="2" fill="none"/></svg></span>
</article>

<article class="abs note note-green" style="left:355px;top:775px;height:62px;padding-top:29px">
  <div class="t">Lorem ipsum dolor</div>
  <p class="d">Lorem ipsum dolor sit amet conse-ctetur adipscing elt...</p>
  <span class="go"><svg width="7" height="9" viewBox="0 0 7 9"><path d="M1 1l4 3.5L1 8" stroke="#fff" stroke-width="2" fill="none"/></svg></span>
</article>
<article class="abs note note-green" style="left:355px;top:841px;height:60px">
  <div class="t">Lorem ipsum dolor</div>
  <p class="d">Lorem ipsum dolor sit amet conse-ctetur adipscing elt...</p>
  <span class="go"><svg width="7" height="9" viewBox="0 0 7 9"><path d="M1 1l4 3.5L1 8" stroke="#fff" stroke-width="2" fill="none"/></svg></span>
</article>
<article class="abs note note-green" style="left:355px;top:905px;height:61px">
  <div class="t">Lorem ipsum dolor</div>
  <p class="d">Lorem ipsum dolor sit amet conse-ctetur adipscing elt...</p>
  <span class="go"><svg width="7" height="9" viewBox="0 0 7 9"><path d="M1 1l4 3.5L1 8" stroke="#fff" stroke-width="2" fill="none"/></svg></span>
</article>
<article class="abs card" style="left:355px;top:971px;height:179px;width:139px">
  <div class="card-img" role="img" aria-label="Photo of an outdoor movie screen at dusk" style="background:linear-gradient(170deg,#4a5a78,#2a3324)"></div>
  <div class="card-title">Lorem ipsum dolor</div>
  <p class="card-text">Lorem ipsum dolor sit amet consectetur adipscing elt, Sed do incidunt magna aliqua...</p>
  <span class="go"><svg width="7" height="9" viewBox="0 0 7 9"><path d="M1 1l4 3.5L1 8" stroke="#fff" stroke-width="2" fill="none"/></svg></span>
</article>

<article class="abs card" style="left:500px;top:775px;height:191px">
  <div class="card-img" role="img" aria-label="Photo of a woman standing in a desert" style="background:linear-gradient(180deg,#f3eee6,#c9aa80)"></div>
  <div class="card-title">Lorem ipsum dolor</div>
  <p class="card-text">Lorem ipsum dolor sit amet consectetur adipscing elt, Sed do euismod tempor incidunt magna aliqua...</p>
  <span class="go"><svg width="7" height="9" viewBox="0 0 7 9"><path d="M1 1l4 3.5L1 8" stroke="#fff" stroke-width="2" fill="none"/></svg></span>
</article>
<article class="abs note note-blue" style="left:500px;top:971px;height:87px;width:138px;padding-top:12px">
  <div class="t">Lorem ipsum dolor</div>
  <p class="d">Lorem ipsum dolor sit amet consectetur adipscing elt, Sed do euismod tempor incidunt magna aliqua...</p>
  <span class="go"><svg width="7" height="9" viewBox="0 0 7 9"><path d="M1 1l4 3.5L1 8" stroke="#fff" stroke-width="2" fill="none"/></svg></span>
</article>
<article class="abs note note-blue" style="left:500px;top:1062px;height:88px;width:138px;padding-top:12px">
  <div class="t">Lorem ipsum dolor</div>
  <p class="d">Lorem ipsum dolor sit amet consectetur adipscing elt, Sed do euismod tempor incidunt magna aliqua...</p>
  <span class="go"><svg width="7" height="9" viewBox="0 0 7 9"><path d="M1 1l4 3.5L1 8" stroke="#fff" stroke-width="2" fill="none"/></svg></span>
</article>

<footer class="abs footer">Copyrights © 2013 tessaly.com - All Rights Reserved</footer>

</body>
</html>
```